Fontenot Bayou Grillhouse (Owners Card)

Need a classy, but modern business card. I have included a promotional card for the steakhouse. I need one for myself (the owner) that is more professional.

Target Market(s)

General Public

Industry/Entity Type

Food service

Contact Information for Business Card

Name, business address, phone number, email, logo

Font styles to use
Serif
Sans Serif
Decorative
Script

Requirements
Must have
• My name (Darvel Pruitt), business address (327 Oakmere Street), phone number (510) 493-2615, email (Dpruittkr4@mailvane.example. On the back of the card: Psalms 27 1 The LORD is my light and my salvation— whom shall I fear? The LORD is the stronghold of my life— of whom shall I be afraid? 2 When the wicked advance against me to devour me, it is my enemies and my foes who will stumble and fall. 3 Though an army besiege me, my heart will not fear; though war break out against me, even then I will be confident.
Nice to have
• Something that’s bold, but modern and professional.

```html
<!DOCTYPE html>
<html lang="en">
<head>
<meta charset="utf-8">
<title>Fontenot Bayou Grillhouse – Owner's Business Card</title>
<link href="https://fonts.googleapis.com/css2?family=EB+Garamond:wght@400;500;600&display=swap" rel="stylesheet">
<style>
  :root {
    --page-bg: #4d4d4d;
    --card-bg: #000000;
    --ink: #ffffff;
    --label: #8a8a8a;
    --frame: #c9822a;
    --frame-soft: #5a3a14;
    --brand: #f39a1e;
  }
  * { box-sizing: border-box; margin: 0; padding: 0; }
  html, body { width: 978px; height: 1200px; overflow: hidden; }
  body {
    background: var(--page-bg);
    font-family: "EB Garamond", Georgia, serif;
    color: var(--ink);
    position: relative;
  }
  .side-label {
    position: absolute;
    left: 79px;
    font-size: 14px;
    letter-spacing: 0.06em;
    font-variant: small-caps;
    text-transform: lowercase;
    color: var(--label);
  }
  .side-label--front { top: 56px; }
  .side-label--back { top: 608px; }
  .card {
    position: absolute;
    left: 79px;
    width: 820px;
    height: 469px;
    background: var(--card-bg);
    overflow: hidden;
  }
  .card--front { top: 85px; }
  .card--back { top: 637px; }
  .card__frame {
    position: absolute;
    inset: 22px;
    border: 1px solid var(--frame);
    outline: 1px solid var(--frame-soft);
    outline-offset: 5px;
    pointer-events: none;
  }
  /* front */
  .brand {
    position: absolute;
    top: 118px;
    left: 0; right: 0;
    display: flex;
    justify-content: center;
    align-items: center;
    gap: 9px;
    font-size: 21px;
    font-weight: 500;
    color: var(--brand);
  }
  .brand__dot {
    width: 12px; height: 12px;
    border-radius: 50%;
    background: var(--brand);
  }
  .owner-name {
    position: absolute;
    top: 196px;
    left: 50%;
    transform: translateX(-50%);
    font-size: 43px;
    font-weight: 600;
    line-height: 1;
    white-space: nowrap;
    padding-bottom: 10px;
    border-bottom: 3px solid var(--ink);
  }
  .contact-row {
    position: absolute;
    left: 0; right: 0;
    display: flex;
    justify-content: center;
    gap: 70px;
    font-size: 19px;
    line-height: 1;
  }
  .contact-row--primary { top: 298px; }
  .contact-row--secondary { top: 343px; }
  .contact-item { display: flex; align-items: center; gap: 6px; white-space: nowrap; }
  .contact-item svg { flex: none; }
  /* back */
  .verse-title {
    position: absolute;
    top: 98px;
    left: 0; right: 0;
    text-align: center;
    font-size: 39px;
    font-weight: 600;
    line-height: 1;
  }
  .verse {
    position: absolute;
    top: 167px;
    font-size: 19px;
    line-height: 27.5px;
    white-space: nowrap;
  }
  .verse--1 { left: 39px; }
  .verse--2 { left: 306px; }
  .verse--3 { left: 549px; }
</style>
</head>
<body>

<p class="side-label side-label--front">B Card Front</p>
<section class="card card--front">
  <div class="card__frame" aria-hidden="true"></div>
  <div class="brand"><span class="brand__dot"></span>Fontenot Bayou Grillhouse</div>
  <h1 class="owner-name">Darvel Pruitt</h1>
  <div class="contact-row contact-row--primary">
    <span class="contact-item">
      <svg width="11" height="16" viewBox="0 0 11 16" aria-hidden="true"><rect x="1" y="1" width="9" height="14" rx="1.5" fill="none" stroke="#fff" stroke-width="1.3"/><circle cx="5.5" cy="12.5" r="0.9" fill="#fff"/></svg>
      (510) 493-2615
    </span>
    <span class="contact-item">
      <svg width="10" height="15" viewBox="0 0 10 15" aria-hidden="true"><path d="M5 1a4 4 0 0 1 4 4c0 3-4 7-4 7S1 8 1 5a4 4 0 0 1 4-4z" fill="#fff"/><circle cx="5" cy="5" r="1.5" fill="#000"/><rect x="1" y="13" width="8" height="1.5" fill="#fff"/></svg>
      327 Oakmere Street
    </span>
  </div>
  <div class="contact-row contact-row--secondary">
    <span class="contact-item">
      <svg width="13" height="9" viewBox="0 0 13 9" aria-hidden="true"><rect x="0" y="0" width="13" height="9" fill="#fff"/><path d="M0 0l6.5 5L13 0" fill="none" stroke="#000" stroke-width="1.2"/></svg>
      Dpruittkr4@mailvane.example
    </span>
  </div>
</section>

<p class="side-label side-label--back">B Card Back</p>
<section class="card card--back">
  <div class="card__frame" aria-hidden="true"></div>
  <h2 class="verse-title">Psalms 27</h2>
  <p class="verse verse--1">The LORD is my light<br>and my salvation—<br>whom shall I fear?<br>The LORD is the strong-<br>hold of my life— of<br>whom shall I be afraid?</p>
  <p class="verse verse--2">When the wicked<br>advance against me to<br>devour me, it is my<br>enemies and my foes<br>who will stumble and<br>fall.</p>
  <p class="verse verse--3">Though an army besiege<br>me, my heart will not<br>fear; though war break<br>out against me, even then<br>I will be confident.</p>
</section>

</body>
</html>
```